Business card

would like a double sided business card made up with my logos provided.
Prefer card to have black background and to use the black logos, with matching blue writing for the text.
One side to just be the logo, (Try to use both the black logos)
the other side to have the logo and also my credentials/business information.

Covering all aspects of Carpentry and Building Services

Marcus Thelwin
Qualified Carpenter
Mob: 0417263985
Email: rkt.joinery@fernmail.example
ABN: 47 619 283 504

Industry/Entity Type

Business

Contact Information for Business Card

Marcus Thelwin
Qualified Carpenter
Mob: 0417263985
ABN: 47 619 283 504

Requirements
Must have
• Please try to use both the black logos and incorporate into the card.

```html
<!DOCTYPE html>
<html lang="en">
<head>
<meta charset="utf-8">
<title>RKT Joinery – Business Card</title>
<link rel="stylesheet" href="https://fonts.googleapis.com/css2?family=Lato:wght@400;700;900&display=swap">
<style>
  :root {
    --stage: #3a3a3a;
    --card: #161616;
    --card-edge: #232323;
    --blue: #1f77c4;
    --white: #f2f2f2;
    --grey: #c9c9c9;
  }
  * { box-sizing: border-box; margin: 0; padding: 0; }
  html, body { width: 1200px; height: 997px; overflow: hidden; }
  body {
    background: var(--stage);
    font-family: "Lato", Arial, sans-serif;
    position: relative;
  }
  .card {
    position: absolute;
    width: 560px;
    height: 320px;
    background: var(--card);
    border: 1px solid var(--card-edge);
    border-radius: 22px;
    box-shadow: 0 18px 40px rgba(0,0,0,.55);
    color: var(--white);
  }
  .card--front { left: 70px; top: 150px; }
  .card--back  { left: 570px; top: 500px; }

  /* Brand wordmark */
  .brand { display: flex; flex-direction: column; }
  .brand__name {
    display: flex; align-items: center; gap: 12px;
    font-weight: 900; color: var(--white); letter-spacing: 2px; line-height: 1;
  }
  .brand__mark { width: 14px; height: 14px; background: var(--blue); }
  .brand__tagline {
    color: var(--blue); font-weight: 700; letter-spacing: 3px;
    text-transform: uppercase;
  }

  /* Front side */
  .card--front .brand { position: absolute; left: 0; right: 0; top: 78px; align-items: center; }
  .card--front .brand__name { font-size: 46px; }
  .card--front .brand__tagline { font-size: 12px; margin-top: 10px; }
  .services {
    position: absolute; left: 0; right: 0; top: 198px;
    text-align: center; text-transform: uppercase; font-weight: 700;
  }
  .services__intro { color: var(--grey); font-size: 17px; letter-spacing: 1.5px; }
  .services__main { color: var(--blue); font-size: 15px; letter-spacing: 3px; margin-top: 8px; }

  /* Back side */
  .card--back .brand { position: absolute; left: 40px; top: 60px; }
  .card--back .brand__name { font-size: 52px; }
  .card--back .brand__tagline { font-size: 12px; margin-top: 10px; }
  .person { position: absolute; right: 40px; top: 138px; text-align: right; }
  .person__name { color: var(--blue); font-weight: 700; font-size: 20px; }
  .person__role { color: var(--white); font-weight: 700; font-size: 12px; letter-spacing: .5px; margin-top: 4px; }
  .divider {
    position: absolute; left: 40px; right: 40px; top: 194px;
    height: 3px; background: var(--blue);
  }
  .contacts { position: absolute; left: 40px; top: 218px; list-style: none; }
  .contacts li {
    display: flex; align-items: center; gap: 14px;
    color: var(--blue); font-weight: 700; font-size: 15px; margin-bottom: 14px;
  }
  .contacts svg { width: 20px; height: 20px; flex: none; }
  .abn { position: absolute; right: 40px; top: 214px; font-weight: 700; font-size: 16px; color: var(--grey); }
  .abn__label { color: var(--blue); }
</style>
</head>
<body>

  <section class="card card--front" aria-label="Card front">
    <div class="brand">
      <div class="brand__name"><span class="brand__mark"></span>RKT JOINERY</div>
      <div class="brand__tagline">Carpenters and Builders</div>
    </div>
    <div class="services">
      <p class="services__intro">Covering all aspects of</p>
      <p class="services__main">Carpentry &amp; Building Services</p>
    </div>
  </section>

  <section class="card card--back" aria-label="Card back">
    <div class="brand">
      <div class="brand__name"><span class="brand__mark"></span>RKT JOINERY</div>
      <div class="brand__tagline">Carpenters and Builders</div>
    </div>

    <div class="person">
      <p class="person__name">Marcus Thelwin</p>
      <p class="person__role">QUALIFIED CARPENTER</p>
    </div>

    <div class="divider"></div>

    <ul class="contacts">
      <li>
        <svg viewBox="0 0 20 20" aria-hidden="true"><rect x="5" y="1.5" width="10" height="17" rx="2" fill="none" stroke="#f2f2f2" stroke-width="1.6"/><line x1="8.5" y1="15.5" x2="11.5" y2="15.5" stroke="#f2f2f2" stroke-width="1.4"/></svg>
        0417263985
      </li>
      <li>
        <svg viewBox="0 0 20 20" aria-hidden="true"><rect x="2" y="4.5" width="16" height="11" fill="#f2f2f2"/><polyline points="2,4.5 10,11 18,4.5" fill="none" stroke="#161616" stroke-width="1.4"/></svg>
        rkt.joinery@fernmail.example
      </li>
    </ul>

    <p class="abn"><span class="abn__label">ABN:</span> 47 619 283 504</p>
  </section>

</body>
</html>
```